Turning fine print into insight is a show dedicated to helping plan fiduciaries close the gap between ERISA participant disclosures and employees, understanding, and attaining actual knowledge of their plan.

Target Market(s)

Retirement Plan Sponsors

Industry/Entity Type

Financial

Colors
0054AA
0677BA
7BADD7
CADEEF
E8F1F8

Requirements
Must have
• Turning Fine Print Into Insight

```html
<!DOCTYPE html>
<html lang="en">
<head>
<meta charset="utf-8">
<title>Turning Fine Print Into Insight — Podcast Cover</title>
<link rel="stylesheet" href="https://fonts.googleapis.com/css2?family=Roboto+Slab:wght@800&family=Roboto+Condensed:wght@300;700&family=Roboto:wght@900&display=swap">
<style>
  :root {
    --brand-blue: #0E77BA;
    --deep-blue: #0054AA;
    --mid-blue: #7BADD7;
    --pale-blue: #CADEEF;
    --mist: #E8F1F8;
    --white: #FFFFFF;
  }
  html, body {
    margin: 0;
    width: 1200px;
    height: 1200px;
    overflow: hidden;
    background: var(--white);
  }
  .cover { display: block; width: 1200px; height: 1200px; }
  .cover__panel { fill: var(--brand-blue); }
  .cover__frame { fill: none; stroke: var(--brand-blue); stroke-width: 4; }
  .cover__frame--on-panel { stroke: var(--white); }
  .title-line {
    font-family: "Roboto Slab", serif;
    font-weight: 800;
    fill: var(--brand-blue);
  }
  .badge__box { fill: var(--brand-blue); }
  .badge__label {
    font-family: "Roboto", sans-serif;
    font-weight: 900;
    font-size: 46px;
    fill: var(--white);
  }
  .host {
    font-family: "Roboto Condensed", sans-serif;
    font-size: 72px;
    fill: var(--brand-blue);
  }
  .host--on-portrait { fill: var(--white); }
  .host__with { font-weight: 300; }
  .host__name { font-weight: 700; }
</style>
</head>
<body>
<svg class="cover" viewBox="0 0 1200 1200" xmlns="http://www.w3.org/2000/svg">
  <defs>
    <linearGradient id="portrait-tone" x1="0" y1="0" x2="0" y2="1">
      <stop offset="0" stop-color="#CADEEF"/>
      <stop offset="0.42" stop-color="#E8F1F8"/>
      <stop offset="0.55" stop-color="#7BADD7"/>
      <stop offset="0.68" stop-color="#0E77BA"/>
      <stop offset="1" stop-color="#0E77BA"/>
    </linearGradient>
    <clipPath id="panel-clip"><rect x="740" y="2" width="460" height="1198"/></clipPath>
    <clipPath id="portrait-clip">
      <path d="M421 1200 L470 900 Q560 760 700 700 L700 160 Q900 120 1090 200 L1110 700 Q1140 780 1170 1200 Z"/>
    </clipPath>
  </defs>

  <rect class="cover__panel" x="740" y="2" width="460" height="1198"/>

  <path class="cover__frame" d="M1143 604 V55 H56 V1142 H700"/>
  <path class="cover__frame cover__frame--on-panel" clip-path="url(#panel-clip)" d="M1143 604 V55 H56 V1142 H700"/>

  <path class="portrait" role="img" aria-label="Two-tone blue portrait illustration of the podcast host in suit and tie"
        fill="url(#portrait-tone)"
        d="M421 1200 L470 900 Q560 760 700 700 L700 160 Q900 120 1090 200 L1110 700 Q1140 780 1170 1200 Z"/>

  <g class="title">
    <text class="title-line" x="147" y="243" font-size="134" textLength="422" lengthAdjust="spacingAndGlyphs">TURNING</text>
    <text class="title-line" x="155" y="333" font-size="92" textLength="406" lengthAdjust="spacingAndGlyphs">FINE PRINT</text>
    <text class="title-line" x="147" y="455" font-size="140" textLength="422" lengthAdjust="spacingAndGlyphs">INTO</text>
    <text class="title-line" x="147" y="736" font-size="300" textLength="422" lengthAdjust="spacingAndGlyphs">INSIGHT</text>
  </g>

  <g class="badge">
    <rect class="badge__box" x="146" y="757" width="362" height="65"/>
    <text class="badge__label" x="165" y="806" textLength="326" lengthAdjust="spacing">PODCAST</text>
  </g>

  <text class="host" x="149" y="1086"><tspan class="host__with">WITH </tspan><tspan class="host__name">DANA HOLLIS</tspan></text>
  <text class="host host--on-portrait" x="149" y="1086" clip-path="url(#portrait-clip)"><tspan class="host__with">WITH </tspan><tspan class="host__name">DANA HOLLIS</tspan></text>
</svg>
</body>
</html>
```